Brolvane Co.,Ltd. need business card

Brolvane Company Limited is a facility management company. We provides a total solution services from administration, energy saving, security, safety, food catering to companies.

The logo should be in elegant style with innovative that suited to the upper market
Please see the logo image in the attached file. You can use this Red or Blue or Green checkerboard (color and font should be similar to logo) as the main part of business card (can be an entire of one side of business card) . In another side of card should contain contact details of personnel - here below demo information

Kanyarat Thoengsai
Chief Executive Officer

No.73, Soi 5, Ruam Wongsa Road
Nong Khaem, Bangkok,
10520, Thailand

Tel + 66841537296
Mobile + 66841537296
E-mail: Kanyarat.Thoengsai@brolvane-example.co.th

Target Market(s)

Factory, Hotel and Hospital

Industry/Entity Type

Business

Contact Information for Business Card

Kanyarat Thoengsai
Chief Executive Officer

Nong Khaem, Bangkok,
10520, Thailand

Tel + 66841537296
Mobile + 66841537296

We will change details with the winner designer

Font styles to use
Sans Serif

Requirements
Must have
• In style of red checkerboard and white color

```html
<!DOCTYPE html>
<html lang="en">
<head>
<meta charset="utf-8">
<title>Brolvane Co.,Ltd. – Business Card</title>
<link rel="stylesheet" href="https://fonts.googleapis.com/css2?family=Lato:wght@300;400;700;900&display=swap">
<style>
  :root {
    --brand-red: #c21f30;
    --brand-red-deep: #8e1220;
    --brand-red-light: #d8404f;
    --accent-pink: #e9546b;
    --charcoal: #2a2a2c;
    --charcoal-light: #3a3a3d;
    --paper: #ffffff;
    --stage: #ecebe8;
    --text-light: #f2f2f2;
  }
  * { box-sizing: border-box; margin: 0; padding: 0; }
  html, body {
    width: 1200px; height: 913px; overflow: hidden;
    background: var(--stage);
    font-family: "Lato", Arial, sans-serif;
  }
  .canvas {
    width: 1200px; height: 913px;
    display: flex; flex-direction: column; align-items: center;
    justify-content: center; gap: 33px;
  }
  .card {
    position: relative; width: 700px; height: 400px;
    border-radius: 4px; overflow: hidden;
    box-shadow: 0 6px 18px rgba(0,0,0,.18);
  }

  /* Front side */
  .card-front { background: var(--brand-red); }
  .front-pattern {
    position: absolute; inset: 0;
    background: linear-gradient(135deg, var(--brand-red-light) 0%, var(--brand-red) 45%, var(--brand-red-deep) 100%);
  }
  .front-wordmark {
    position: absolute; inset: 0;
    display: flex; align-items: center; justify-content: center;
    color: var(--paper); font-weight: 400; font-size: 86px;
    letter-spacing: 14px;
  }

  /* Back side */
  .card-back { background: var(--paper); }
  .back-wordmark {
    position: absolute; left: 40px; top: 196px;
    color: var(--brand-red); font-weight: 400; font-size: 38px;
    letter-spacing: 6px;
  }
  .name-band {
    position: absolute; left: 360px; right: 0; top: 62px; height: 82px;
    background: var(--accent-pink); color: var(--paper);
    padding: 16px 22px;
  }
  .person-name { font-size: 22px; line-height: 1.1; letter-spacing: .5px; }
  .person-name .given { font-weight: 900; }
  .person-name .family { font-weight: 300; }
  .person-title { font-size: 15px; font-weight: 300; margin-top: 4px; }
  .contact-band {
    position: absolute; left: 0; right: 0; top: 256px; height: 100px;
    background:
      repeating-linear-gradient(135deg, rgba(255,255,255,.04) 0 1px, transparent 1px 5px),
      linear-gradient(90deg, var(--charcoal) 0%, var(--charcoal-light) 100%);
    color: var(--text-light); font-size: 13.5px; font-weight: 400;
    padding: 14px 30px;
  }
  .address { letter-spacing: .2px; }
  .contact-rows { display: flex; justify-content: space-between; margin-top: 14px; }
  .contact-list { list-style: none; display: flex; flex-direction: column; gap: 8px; }
  .contact-item { display: flex; align-items: center; gap: 10px; }
  .icon { width: 22px; height: 18px; flex: none; }
</style>
</head>
<body>
<main class="canvas">
  <section class="card card-front" aria-label="Card front">
    <div class="front-pattern" role="img" aria-label="Red checkerboard background pattern"></div>
    <div class="front-wordmark">BROLVANE</div>
  </section>

  <section class="card card-back" aria-label="Card back">
    <div class="back-wordmark">BROLVANE</div>

    <div class="name-band">
      <div class="person-name"><span class="given">KANYARAT</span> <span class="family">THOENGSAI</span></div>
      <div class="person-title">Chief Executive Officer</div>
    </div>

    <div class="contact-band">
      <p class="address">No.73, Soi 5, Ruam Wongsa Road, Nong Khaem, Bangkok, 10520, Thailand</p>
      <div class="contact-rows">
        <ul class="contact-list">
          <li class="contact-item">
            <svg class="icon" viewBox="0 0 22 18" aria-hidden="true">
              <rect width="22" height="18" rx="3" fill="#e2263a"/>
              <path d="M6 6c0-1.5 10-1.5 10 0v1.5h-2.5V6.5h-5v1h-2.5z M7 9h8l1 5H6z" fill="#fff"/>
            </svg>
            <span>+ 66841537296</span>
          </li>
          <li class="contact-item">
            <svg class="icon" viewBox="0 0 22 18" aria-hidden="true">
              <rect width="22" height="18" rx="3" fill="#e2263a"/>
              <rect x="7.5" y="3.5" width="7" height="4" fill="#fff"/>
              <rect x="5" y="7.5" width="12" height="5" rx="1" fill="#fff"/>
              <rect x="7.5" y="11" width="7" height="3.5" fill="#fff" stroke="#e2263a" stroke-width=".8"/>
            </svg>
            <span>+ 66841537296</span>
          </li>
        </ul>
        <ul class="contact-list">
          <li class="contact-item">
            <svg class="icon" viewBox="0 0 22 18" aria-hidden="true">
              <rect width="22" height="18" rx="3" fill="#e2263a"/>
              <rect x="5" y="5" width="12" height="8" fill="#fff"/>
              <path d="M5 5l6 5 6-5" fill="none" stroke="#e2263a" stroke-width="1.2"/>
            </svg>
            <span>Kanyarat.Thoengsai@brolvane-example.co.th</span>
          </li>
        </ul>
      </div>
    </div>
  </section>
</main>
</body>
</html>
```